KTRL Business Card Design

Business card for sole operator professional civil and traffic engineer.
Clients are developers and planners who require assistance with traffic strategic master planning advice and design development for access and infrastructure associated with the development.
Colours already in use are greens for the business name and black for other legend. The attached file shows the letterhead template which is currently in use.
Target Market(s)
Professional Clients in development industry
Most clients known to the Principal and card is mostly required to allow ongoing contact
Industry/Entity Type
Business
Contact Information for Business Card
DONALD PLUMWEATHER ADVISORY SERVICES
ABN 37 806 519 174
PO Box 718 KELVALE NSW 2461
Donald Plumweather 0413 885 190
donald.plumweather@farvenmail.com

```html
<!DOCTYPE html>
<html lang="en">
<head>
<meta charset="UTF-8">
<title>KTRL Business Card</title>
<link href="https://fonts.googleapis.com/css2?family=Lato:wght@400;700;900&display=swap" rel="stylesheet">
<style>
  :root {
    --page-bg: #e9ebe6;
    --lime: #8fcb3c;
    --lime-light: #a6d957;
    --forest: #1f6b2a;
    --deep-green: #0f4a1c;
    --rule: #d9f0b8;
    --ink: #1c2a1c;
  }
  * { margin: 0; padding: 0; box-sizing: border-box; }
  html, body {
    width: 1200px;
    height: 841px;
    overflow: hidden;
    background: var(--page-bg);
    font-family: "Lato", Arial, sans-serif;
  }
  .card {
    position: absolute;
    left: 100px;
    top: 115px;
    width: 1000px;
    height: 611px;
    background: var(--lime);
    overflow: hidden;
    box-shadow: 0 10px 30px rgba(0,0,0,0.18);
  }
  .blueprint-band {
    position: absolute;
    left: 0;
    width: 100%;
  }
  .blueprint-band--top {
    top: 0;
    height: 128px;
    background: linear-gradient(100deg, var(--forest) 0%, var(--lime-light) 45%, var(--lime) 100%);
  }
  .blueprint-band--bottom {
    bottom: 0;
    height: 200px;
    background: linear-gradient(95deg, var(--deep-green) 0%, var(--forest) 35%, #5fa83a 70%, var(--lime) 100%);
  }
  .band-rule {
    position: absolute;
    left: 0;
    width: 100%;
    height: 6px;
    background: var(--rule);
    opacity: 0.85;
  }
  .band-rule--top { top: 128px; }
  .band-rule--bottom { bottom: 200px; }
  .details {
    position: absolute;
    left: 0;
    top: 148px;
    width: 100%;
    height: 257px;
    color: var(--ink);
    text-align: center;
  }
  .business-name {
    font-weight: 900;
    font-size: 33px;
    letter-spacing: 0.5px;
    margin-top: 6px;
  }
  .registration, .postal {
    font-weight: 700;
    font-size: 26px;
    line-height: 1.25;
  }
  .principal {
    font-size: 44px;
    font-weight: 400;
    letter-spacing: 1px;
    margin-top: 14px;
  }
  .principal .surname { font-weight: 900; }
  .contact-line {
    position: absolute;
    left: 0;
    right: 0;
    bottom: -2px;
    font-size: 24px;
    font-weight: 400;
    text-align: center;
  }
  .contact-line .label { font-weight: 700; }
  .contact-line .divider { margin: 0 12px; }
</style>
</head>
<body>
  <div class="card">
    <div class="blueprint-band blueprint-band--top" role="img" aria-label="Green-tinted photo of rolled engineering blueprints"></div>
    <div class="band-rule band-rule--top"></div>

    <div class="details">
      <div class="business-name">DONALD PLUMWEATHER ADVISORY SERVICES</div>
      <div class="registration">ABN 37 806 519 174</div>
      <div class="postal">PO Box 718 KELVALE NSW 2461</div>
      <div class="principal">DONALD <span class="surname">PLUMWEATHER</span></div>
      <div class="contact-line">
        <span class="label">PHONE:</span> 0413 885 190<span class="divider">|</span><span class="label">EMAIL:</span> donald.plumweather@farvenmail.com
      </div>
    </div>

    <div class="band-rule band-rule--bottom"></div>
    <div class="blueprint-band blueprint-band--bottom" role="img" aria-label="Green-tinted photo of technical drawings and rolled plans"></div>
  </div>
</body>
</html>
```